Tallowreed Advisory Partners Business Card Design

We have the logo we just need someone to design a modern business card design.

Name: Desmond Munkalt
Phone: 3055550148
Mobile: 9175550193
Web:www.tallowreedadvisory.example
email: dmunkalt@tallowreedadvisory.example
Company: Tallowreed Advisory Partners
Title: CEO

Address: 718 Quillmore Ave, Miami, Florida 33190

Target Market(s)

companies over 100 employees

Industry/Entity Type

Business

```html
<!DOCTYPE html>
<html lang="en">
<head>
<meta charset="utf-8">
<title>Tallowreed Advisory Partners — Business Card</title>
<link rel="stylesheet" href="https://fonts.googleapis.com/css2?family=Archivo:wght@400;700;800&family=Libre+Franklin:wght@400;500&display=swap">
<style>
  :root {
    --backdrop: #d6d7d8;
    --card-navy: #0b1a24;
    --row-dark: #0e1d28;
    --row-slate: #263741;
    --accent-blue: #1a8fd1;
    --text-white: #f2f4f5;
    --text-grey: #7b8790;
    --text-muted: #93a0a8;
    --line-light: rgba(235, 240, 244, 0.8);
  }
  * { box-sizing: border-box; margin: 0; padding: 0; }
  html, body { width: 1200px; height: 1000px; overflow: hidden; }
  body {
    background: var(--backdrop);
    font-family: "Libre Franklin", Arial, sans-serif;
    position: relative;
  }
  .card {
    position: absolute;
    left: 250px;
    width: 700px;
    height: 400px;
    background: var(--card-navy);
    overflow: hidden;
    box-shadow: 0 6px 18px rgba(0, 0, 0, 0.25);
  }
  .card--front { top: 70px; }
  .card--back { top: 530px; }

  .brand-mark {
    display: block;
    border-radius: 50%;
    background: var(--accent-blue);
  }
  .brand-name {
    font-family: "Archivo", Arial, sans-serif;
    font-weight: 800;
    color: var(--text-white);
    text-transform: uppercase;
    letter-spacing: 2px;
    text-align: center;
    line-height: 1.15;
  }

  /* Front */
  .front-lockup {
    position: absolute;
    inset: 0;
    display: flex;
    flex-direction: column;
    align-items: center;
    justify-content: center;
    gap: 22px;
  }
  .front-lockup .brand-mark { width: 110px; height: 110px; }
  .front-lockup .brand-name { font-size: 34px; }

  /* Back */
  .contact-art { position: absolute; left: 0; top: 0; }
  .contact-line {
    position: absolute;
    text-align: right;
    color: var(--text-white);
    font-size: 18px;
    line-height: 1.2;
    letter-spacing: 0.3px;
  }
  .contact-line--web { color: var(--text-muted); }
  .contact-line--social { font-size: 16px; color: var(--text-muted); }
  .contact-line--social .label { color: var(--text-grey); }

  .identity {
    position: absolute;
    left: 430px;
    right: 20px;
    top: 50px;
    display: flex;
    flex-direction: column;
    align-items: center;
  }
  .identity .brand-mark { width: 104px; height: 104px; margin-bottom: 20px; }
  .identity .brand-name { font-size: 25px; }
  .person-name {
    margin-top: 22px;
    font-family: "Archivo", Arial, sans-serif;
    font-weight: 700;
    font-size: 24px;
    color: var(--text-white);
  }
  .person-title {
    font-family: "Archivo", Arial, sans-serif;
    font-weight: 400;
    font-size: 21px;
    color: var(--text-grey);
    margin-top: 2px;
  }
</style>
</head>
<body>

<section class="card card--front" aria-label="Card front">
  <div class="front-lockup">
    <span class="brand-mark" aria-hidden="true"></span>
    <p class="brand-name">Tallowreed<br>Advisory Partners</p>
  </div>
</section>

<section class="card card--back" aria-label="Card back">
  <svg class="contact-art" width="700" height="400" viewBox="0 0 700 400" aria-hidden="true">
    <defs>
      <clipPath id="info-area">
        <path d="M0 0 L380 0 Q300 200 330 400 L0 400 Z"/>
      </clipPath>
      <clipPath id="icon-band">
        <path d="M380 0 Q300 200 330 400 L374 400 Q344 200 424 0 Z"/>
      </clipPath>
    </defs>

    <g class="info-rows" clip-path="url(#info-area)">
      <rect x="0" y="28"  width="400" height="58" fill="var(--row-dark)"/>
      <rect x="0" y="86"  width="400" height="56" fill="var(--row-slate)"/>
      <rect x="0" y="142" width="400" height="58" fill="var(--row-dark)"/>
      <rect x="0" y="200" width="400" height="56" fill="var(--row-slate)"/>
      <rect x="0" y="256" width="400" height="58" fill="var(--row-dark)"/>
      <rect x="0" y="314" width="400" height="58" fill="var(--row-slate)"/>
    </g>

    <g class="icon-cells" clip-path="url(#icon-band)">
      <rect x="280" y="0"   width="160" height="86" fill="var(--accent-blue)"/>
      <rect x="280" y="86"  width="160" height="56" fill="var(--row-dark)"/>
      <rect x="280" y="142" width="160" height="58" fill="var(--accent-blue)"/>
      <rect x="280" y="200" width="160" height="56" fill="var(--row-dark)"/>
      <rect x="280" y="256" width="160" height="58" fill="var(--accent-blue)"/>
      <rect x="280" y="314" width="160" height="86" fill="var(--row-dark)"/>
      <g stroke="var(--line-light)" stroke-width="1.5">
        <line x1="280" y1="86"  x2="440" y2="86"/>
        <line x1="280" y1="142" x2="440" y2="142"/>
        <line x1="280" y1="200" x2="440" y2="200"/>
        <line x1="280" y1="256" x2="440" y2="256"/>
        <line x1="280" y1="314" x2="440" y2="314"/>
      </g>
    </g>

    <g class="band-edges" fill="none" stroke="var(--line-light)" stroke-width="1.5">
      <path d="M380 0 Q300 200 330 400"/>
      <path d="M424 0 Q344 200 374 400"/>
    </g>

    <g class="icons" fill="none" stroke="#ffffff" stroke-width="1.8" stroke-linecap="round" stroke-linejoin="round">
      <!-- mobile -->
      <rect x="376" y="46" width="13" height="22" rx="2"/>
      <line x1="381" y1="64" x2="384" y2="64"/>
      <!-- envelope -->
      <rect x="356" y="106" width="22" height="15"/>
      <path d="M356 106 L367 115 L378 106"/>
      <!-- phone handset -->
      <path d="M345 163 q-3 3 0 8 q5 8 12 11 q5 2 7 -1 l-4 -4 l-3 2 q-5 -3 -7 -8 l2 -3 Z"/>
      <!-- pin -->
      <path d="M347 240 q-8 -10 -8 -15 a8 8 0 0 1 16 0 q0 5 -8 15 Z"/>
      <circle cx="347" cy="225" r="2.5"/>
      <!-- globe -->
      <circle cx="345" cy="285" r="10"/>
      <ellipse cx="345" cy="285" rx="4.5" ry="10"/>
      <line x1="335" y1="285" x2="355" y2="285"/>
      <!-- monitor -->
      <rect x="335" y="334" width="22" height="15" rx="1"/>
      <line x1="346" y1="349" x2="346" y2="354"/>
      <line x1="340" y1="355" x2="352" y2="355"/>
    </g>
  </svg>

  <p class="contact-line" style="right:352px; top:46px;">(917) 555-0193</p>
  <p class="contact-line" style="right:368px; top:92px;">dmunkalt@<br>tallowreedadvisory.example</p>
  <p class="contact-line" style="right:380px; top:160px;">(305) 555-0148</p>
  <p class="contact-line" style="right:387px; top:206px;">718 Quillmore Ave,<br>Miami, Florida 33190</p>
  <p class="contact-line contact-line--web" style="right:390px; top:274px;">www.tallowreedadvisory.example</p>
  <p class="contact-line contact-line--social" style="right:389px; top:322px;"><span class="label">FB:</span> Tallowreed Advisory Partners<br><span class="label">Twitter:</span> @TAP72</p>

  <div class="identity">
    <span class="brand-mark" aria-hidden="true"></span>
    <p class="brand-name">Tallowreed<br>Advisory Partners</p>
    <p class="person-name">Desmond Munkalt</p>
    <p class="person-title">CEO/President</p>
  </div>
</section>

</body>
</html>
```